Communications & Broadcast Consulting/PR/Media Relations & Public Affairs

My main goals are to provide communications support to school districts, small towns/cities/hospitals and private businesses in the form of press releases, media relations, public affairs. I also have 25 years experience as a television news anchor/reporter and I'm open to free-lance reporting in both Indianapolis and other markets. My specialty is working with the media.
Communications

```html
<!DOCTYPE html>
<html lang="en">
<head>
<meta charset="utf-8">
<title>Northbeam Communications – Business Card</title>
<link rel="stylesheet" href="https://fonts.googleapis.com/css2?family=Cinzel:wght@400;600;700&display=swap">
<style>
  :root {
    --backdrop: #ece8e1;
    --card: #fbfbfa;
    --card-shade: #eeeeec;
    --ink: #4a4a4a;
    --ink-soft: #5c5c5c;
    --gold: #f2a91e;
    --green: #8cc22a;
    --tower-faint: #e4e4e2;
  }
  * { margin: 0; padding: 0; box-sizing: border-box; }
  html, body {
    width: 1200px; height: 821px; overflow: hidden;
    background: var(--backdrop);
  }
  .card {
    position: absolute; left: 390px; top: 45px;
    width: 420px; height: 730px;
    background: linear-gradient(180deg, var(--card) 0%, var(--card-shade) 100%);
    box-shadow: 0 6px 24px rgba(0,0,0,.18);
    font-family: "Cinzel", serif;
    color: var(--ink);
    overflow: hidden;
  }
  .tower-art {
    position: absolute; right: 0; top: 190px;
    width: 260px; height: 540px;
    background: linear-gradient(180deg, rgba(228,228,226,0) 0%, var(--tower-faint) 45%, rgba(228,228,226,.6) 100%);
  }
  .edge-band { position: absolute; width: 14px; height: 70px; background: var(--green); }
  .edge-band.left { left: 0; top: 268px; }
  .edge-band.right { right: 0; top: 545px; }
  .brand {
    position: absolute; left: 0; right: 0; top: 190px;
    display: flex; align-items: center; justify-content: center; gap: 12px;
    font-weight: 600; font-size: 27px; letter-spacing: 1px; color: var(--ink);
  }
  .brand-dot { width: 14px; height: 14px; border-radius: 50%; background: var(--green); }
  .holder { position: absolute; left: 50px; right: 30px; top: 300px; }
  .holder-name { font-size: 30px; font-weight: 700; color: var(--gold); letter-spacing: .5px; }
  .holder-role { font-size: 14px; font-weight: 600; color: var(--ink-soft); margin-top: 4px; }
  .rule { height: 2px; background: var(--gold); width: 300px; margin: 18px 0; }
  .contact { list-style: none; padding-left: 70px; }
  .contact li {
    display: flex; align-items: center; gap: 8px;
    font-size: 17px; font-weight: 600; margin-bottom: 6px;
  }
  .contact svg { width: 16px; height: 16px; flex: none; }
  .address { text-align: center; margin-top: 4px; font-size: 17px; font-weight: 600; line-height: 1.5; }
  .address svg { width: 22px; height: 22px; display: block; margin: 0 auto 8px; }
</style>
</head>
<body>
  <article class="card">
    <div class="tower-art" role="img" aria-label="Faint radio tower illustration in the card background"></div>
    <span class="edge-band left"></span>
    <span class="edge-band right"></span>

    <header class="brand">
      <span class="brand-dot"></span>
      <span class="brand-name">Northbeam Communications</span>
    </header>

    <section class="holder">
      <h1 class="holder-name">Dale Ferris</h1>
      <p class="holder-role">Public &amp; Media Relations Consultant</p>
      <div class="rule"></div>

      <ul class="contact">
        <li>
          <svg viewBox="0 0 16 16"><rect width="16" height="16" rx="2" fill="var(--gold)"/><path d="M5 3.5l2 2-1 1.2c.6 1.4 1.8 2.6 3.2 3.2l1.2-1 2 2-1.3 1.6C7.6 12.4 3.6 8.4 3.5 4.8z" fill="#fff"/></svg>
          317.555.0142
        </li>
        <li>
          <svg viewBox="0 0 16 16"><rect width="16" height="16" rx="2" fill="var(--gold)"/><rect x="5" y="2.5" width="6" height="11" rx="1" fill="#fff"/><rect x="6" y="4" width="4" height="6.5" fill="var(--gold)"/></svg>
          317.555.0187
        </li>
        <li>
          <svg viewBox="0 0 16 16"><rect width="16" height="16" rx="2" fill="var(--gold)"/><rect x="3" y="4.5" width="10" height="7" fill="#fff"/><path d="M3 4.5l5 4 5-4" fill="none" stroke="var(--gold)" stroke-width="1.2"/></svg>
          dferris@example.com
        </li>
      </ul>

      <div class="rule"></div>

      <div class="address">
        <svg viewBox="0 0 22 22"><rect width="22" height="22" rx="3" fill="var(--gold)"/><path d="M11 4a4.5 4.5 0 0 0-4.5 4.5C6.5 12 11 18 11 18s4.5-6 4.5-9.5A4.5 4.5 0 0 0 11 4z" fill="#fff"/><circle cx="11" cy="8.5" r="1.7" fill="var(--gold)"/></svg>
        2210 Alder Court Indianapolis,<br>IN 46201
      </div>
    </section>
  </article>
</body>
</html>
```